Verpackungsdesign  für Gewürzlinie gesucht
Verpackungsdesign für Gewürzlinie gesucht
Zielgruppe
Wir sind ein Lebensmittelhersteller und wollen eine neue Gewürzlinie für hochwertige Gewürze launchen. Hierbei handelt es sich um Gewürze für den Bereich Grillen und Kochen. Unsere Zielgruppe sind Männer sowie Frauen über 20 Jahre. Das Produkt selber soll sehr hochwertig sein, somit soll auch das Design den Premium-Aspekt widerspiegeln.
Die Markenbezeichnung lautet 'Halm & Kessel'.
Aufgabenstellung
In die Verpackung sollen 'Mischungen würzender Zutaten' abgefüllt werden.
Es handelt sich bei der Verpackung um eine Runddose mit Weißblechdeckel- sowie Boden. Die Maße der Verpackung ist 40 mm Durchmesser bei 90 mm Höhe (Template des Herstellers ist bei den angehängten Dateien zu finden). Der Inhalt ist 50 g.
Logodateien sind bereits vorhanden.
Aktuell gibt es 4 verschiedene BBQ Gewürze, die in einem Geschenkset kombiniert werden. Die Bezeichnungen sind:
Donnerkiste, Jadetiger, Wüstenfuchsbau und Nordlichtfeld. Das Gewürz kann auf der Verpackung noch zusätzlich beschrieben werden mit: Donnerkiste (Die Geschmacksexplosion), Jadetiger (Curry trifft BBQ), Wüstenfuchsbau (Fette Beute) und Nordlichtfeld (Eine Prise Urlaub)
Auf die Verpackung müssen zusätzlich noch folgende Informationen:
1. Mischung würzender Zutaten / Seasoning
2. 50 g net.
3. Mindestens haltbar bis: Siehe Boden / Best before: see bottom
4. Das Kreislaufsiegel
WICHTIGER HINWEIS:
Die Produkte kommen in eine Umverpackung auf der die Herstellerangaben, EAN Code, etc. angegeben werden, somit ist das für die eigentliche Produktverpackung nicht relevant.
Dem Produkt liegen noch Karten bei, wo die Nährwertangaben, etc. stehen, somit ist das für die eigentliche Produktverpackung nicht relevant.

```html
<!DOCTYPE html>
<html lang="de">
<head>
<meta charset="utf-8">
<title>Halm &amp; Kessel – Nordlichtfeld Dosenetikett</title>
<link href="https://fonts.googleapis.com/css2?family=Oswald:wght@300;400;600&family=Montserrat:wght@300;400&display=swap" rel="stylesheet">
<style>
  :root{
    --bg-dark:#171717;
    --bg-mid:#262626;
    --panel:#222222;
    --blue:#4a8cef;
    --stripe:rgba(74,120,210,.55);
    --text-grey:#a8a8a8;
    --white:#ffffff;
    --ink:#1e1e1e;
    --seal:#6aa63a;
  }
  html,body{margin:0;padding:0;overflow:hidden;}
  body{width:1200px;height:783px;background:var(--bg-dark);}
  .label{
    position:relative;width:1200px;height:783px;overflow:hidden;
    background:linear-gradient(90deg,#121212 0%,#1e1e1e 50%,#2a2a2a 75%,#1a1a1a 100%);
    font-family:'Oswald',sans-serif;
  }
  .stripes{
    position:absolute;top:0;bottom:0;
    background:repeating-linear-gradient(90deg,transparent 0 16px,var(--stripe) 16px 17px);
  }
  .stripes--left{left:0;width:625px;}
  .stripes--right{left:1055px;width:145px;}
  .stripe-single{position:absolute;top:0;bottom:0;width:1px;background:var(--stripe);left:676px;}

  /* back panel */
  .back-panel{
    position:absolute;left:225px;top:161px;width:279px;height:555px;
    background:var(--panel);
  }
  .brand{color:var(--white);font-weight:400;letter-spacing:1px;margin:0;position:absolute;white-space:nowrap;}
  .back-panel .brand{left:0;right:0;text-align:center;top:34px;font-size:30px;}
  .back-title{
    position:absolute;left:0;right:0;top:108px;text-align:center;margin:0;
    color:var(--blue);font-weight:400;font-size:38px;line-height:1;letter-spacing:.5px;
  }
  .back-title-rule{position:absolute;left:96px;width:85px;top:159px;height:2px;background:var(--blue);}
  .meat-icon{position:absolute;top:184px;width:58px;height:58px;border-radius:50%;background:var(--blue);}
  .meat-icon--1{left:29px}.meat-icon--2{left:112px}.meat-icon--3{left:192px}
  .description{
    position:absolute;left:8px;top:263px;margin:0;width:270px;
    color:var(--text-grey);font-weight:300;font-size:20.5px;line-height:28.4px;text-transform:uppercase;
  }
  .recycle-seal{position:absolute;left:9px;top:502px;width:40px;height:40px;border-radius:50%;background:var(--seal);}
  .legal{
    position:absolute;right:11px;top:500px;margin:0;text-align:right;
    color:var(--blue);font-size:13.5px;line-height:22px;font-weight:400;text-transform:uppercase;
  }

  /* front */
  .front .brand{left:713px;top:66px;font-size:44px;}
  .front-rule{position:absolute;left:708px;top:176px;width:3px;height:535px;background:var(--blue);}
  .front-name{position:absolute;left:722px;top:176px;width:92px;height:537px;}
  .front-name text{font-family:'Oswald',sans-serif;font-weight:600;fill:var(--blue);}
  .flavour-box{position:absolute;left:828px;top:176px;width:200px;height:176px;background:var(--blue);}
  .flavour-type{position:absolute;left:17px;top:16px;margin:0;color:var(--white);font-size:29px;font-weight:400;letter-spacing:.5px;line-height:1.2;}
  .flavour-box-rule{position:absolute;left:0;top:67px;width:49px;height:3px;background:var(--ink);}
  .flavour-claim{position:absolute;left:17px;top:127px;margin:0;color:var(--white);font-size:21px;font-weight:400;letter-spacing:.5px;line-height:1.2;}
  .recipe{position:absolute;right:174px;top:358px;margin:0;color:var(--blue);font-family:'Montserrat',sans-serif;font-weight:300;font-size:16px;}
  .leaf-art{
    position:absolute;left:846px;top:415px;width:182px;height:252px;
    border-radius:55% 45% 50% 50%/60% 55% 45% 40%;
    background:radial-gradient(circle at 45% 45%,rgba(74,140,239,.35),rgba(74,140,239,.12) 70%,transparent 72%);
  }
  .net-weight{position:absolute;left:844px;top:680px;margin:0;color:var(--blue);font-family:'Montserrat',sans-serif;font-weight:300;font-size:17px;white-space:nowrap;}
  .net-weight strong{font-weight:400;font-size:36px;vertical-align:-4px;}
</style>
</head>
<body>
<div class="label">
  <div class="stripes stripes--left"></div>
  <div class="stripe-single"></div>
  <div class="stripes stripes--right"></div>

  <section class="back-panel">
    <p class="brand">Halm &amp; Kessel</p>
    <h2 class="back-title">NORDLICHTFELD</h2>
    <div class="back-title-rule"></div>
    <div class="meat-icon meat-icon--1" role="img" aria-label="Symbol Geflügel"></div>
    <div class="meat-icon meat-icon--2" role="img" aria-label="Symbol Rind"></div>
    <div class="meat-icon meat-icon--3" role="img" aria-label="Symbol Schwein"></div>
    <p class="description">Lorem ipsum dolor sit amet,<br>consectetur adipiscing elit. Quis<br>sit nulla id auctor. Ut ac<br>commodo<br>nisi morbi quisque non. Auctor<br>lacinia commodo pellentesque.<br>Curabitur semper</p>
    <div class="recycle-seal" role="img" aria-label="Das Kreislaufsiegel"></div>
    <p class="legal">Mischung würzender Zutaten<br>Mindestens haltbar bis: siehe Boden</p>
  </section>

  <section class="front">
    <p class="brand">Halm &amp; Kessel</p>
    <div class="front-rule"></div>
    <svg class="front-name" viewBox="0 0 92 537" aria-label="Nordlichtfeld">
      <text transform="translate(88 537) rotate(-90)" font-size="112" textLength="535" lengthAdjust="spacingAndGlyphs">NORDLICHTFELD</text>
    </svg>
    <div class="flavour-box">
      <p class="flavour-type">BBQ GEWÜRZ</p>
      <div class="flavour-box-rule"></div>
      <p class="flavour-claim">EINE PRISE URLAUB</p>
    </div>
    <p class="recipe">ORIGINALREZEPTUR</p>
    <div class="leaf-art" role="img" aria-label="Linienillustration eines Blattes mit Adern"></div>
    <p class="net-weight">NETTO <strong>50</strong> GRAMM</p>
  </section>
</div>
</body>
</html>
```